Wordpress Website for electrician

I'm looking for an easy to maintain website for my electrical contracting business. Need a professional and appealing site.
Im wanting a website where clients can come on and look at services we offer, case studies and advertise our services.
Colours I'm wanting to incorporate are green, white, black and grey
I'm wanting a big slide show on main page where I can place advertising etc.
Menu is to include home, services, our work, specials, energy efficiency and contact
My existing site is www.trelwirefix.com.au
Updates
looking for something with a similar layout to this website
Target Market(s)
Businesses
Industry/Entity Type
Electrician
Look and feel

```html
<!DOCTYPE html>
<html lang="en">
<head>
<meta charset="utf-8">
<title>trelwirefix – Electrical Contractor</title>
<link rel="stylesheet" href="https://fonts.googleapis.com/css2?family=Open+Sans:wght@400;600;700&display=swap">
<style>
  :root {
    --green: #3cb44a;
    --green-dark: #1f9a33;
    --black: #000000;
    --bar: #1e1c1d;
    --text: #222222;
    --muted: #6a6a6a;
    --rule: #cfcfcf;
    --white: #ffffff;
    --sky-deep: #3c78b4;
    --sky-light: #8fbde3;
  }
  * { box-sizing: border-box; margin: 0; padding: 0; }
  html, body { width: 1046px; height: 1200px; overflow: hidden; background: var(--white); }
  body { font-family: "Open Sans", Arial, sans-serif; color: var(--text); position: relative; }

  .site-header { position: absolute; top: 0; left: 0; width: 1046px; height: 123px; }
  .brand { position: absolute; left: 28px; top: 44px; display: flex; align-items: center; gap: 12px; }
  .brand-mark { width: 34px; height: 34px; border-radius: 50%; background: var(--green); }
  .brand-name { font-size: 30px; font-weight: 600; color: #222; letter-spacing: 0.5px; }
  .search { position: absolute; left: 778px; top: 48px; width: 240px; height: 32px; background: var(--green); border: 1px solid var(--green-dark); border-radius: 4px; display: flex; align-items: center; padding: 0 10px; justify-content: space-between; }
  .search span { font-size: 13px; color: #123; letter-spacing: 1px; }

  .main-nav { position: absolute; top: 123px; left: 0; width: 1046px; height: 35px; background: var(--bar); display: flex; justify-content: space-between; align-items: center; padding: 0 27px 0 29px; }
  .main-nav a { color: var(--white); text-decoration: none; font-size: 15px; letter-spacing: 1.3px; }

  .hero { position: absolute; top: 158px; left: 0; width: 1046px; height: 275px; background: linear-gradient(90deg, #4a7fb8 0%, #3f79b6 60%, var(--sky-deep) 66%, var(--sky-light) 100%); }
  .hero-photo { position: absolute; right: 0; top: 0; width: 400px; height: 275px; background: linear-gradient(160deg, #4f87c0 0%, #8fbde3 55%, #dbe9f4 100%); }
  .hero-title { position: absolute; left: 56px; top: 57px; width: 560px; text-align: center; color: var(--white); font-size: 34px; font-weight: 700; font-variant: small-caps; letter-spacing: 2px; line-height: 38px; }
  .hero-arrow { position: absolute; top: 118px; }
  .hero-arrow.prev { left: 14px; }
  .hero-arrow.next { right: 14px; }

  .promo { position: absolute; top: 452px; }
  .promo.left { left: 22px; width: 460px; }
  .promo.right { left: 556px; width: 470px; }
  .promo h2 { font-size: 24px; font-weight: 700; letter-spacing: 2px; line-height: 38px; color: #111; }
  .promo p { font-size: 13px; color: var(--muted); letter-spacing: 1px; line-height: 25.6px; margin-top: 4px; }
  .divider-v { position: absolute; left: 513px; top: 460px; width: 1px; height: 230px; background: var(--rule); }
  .btn { position: absolute; height: 40px; border-radius: 4px; border: 2px solid #bbb; color: var(--white); font-size: 15px; font-weight: 700; font-variant: small-caps; letter-spacing: 1.3px; display: flex; align-items: center; justify-content: center; }
  .btn.dark { background: var(--black); }
  .btn.green { background: var(--green-dark); }

  .rule { position: absolute; left: 17px; width: 1011px; height: 1px; background: var(--rule); }

  .card { position: absolute; top: 755px; width: 310px; height: 222px; border: 2px solid var(--rule); border-radius: 6px; }
  .card h3 { position: absolute; left: 11px; top: 16px; font-size: 22px; font-weight: 700; font-variant: small-caps; letter-spacing: 1.5px; line-height: 30px; border-bottom: 2px solid #222; color: #111; white-space: nowrap; }
  .card p { position: absolute; left: 11px; top: 60px; width: 292px; font-size: 12.5px; color: var(--muted); letter-spacing: 0.7px; line-height: 19px; }
  .card-icon { position: absolute; left: 11px; top: 126px; width: 97px; height: 77px; border: 2px solid #333; display: flex; align-items: center; justify-content: center; }
  .card-icon span { width: 46px; height: 46px; border-radius: 6px; display: block; }
  .card a { position: absolute; left: 120px; top: 155px; font-size: 13px; font-weight: 600; color: var(--green-dark); letter-spacing: 1px; text-decoration: underline; }

  .footer-nav { position: absolute; top: 1056px; left: 0; width: 1046px; text-align: center; font-size: 14px; letter-spacing: 1px; color: #111; }
  .footer-nav span { color: #666; margin: 0 5px; }

  .footer-bar { position: absolute; top: 1105px; left: 0; width: 1046px; height: 53px; background: var(--bar); }
  .copyright { position: absolute; left: 16px; top: 17px; color: var(--white); font-size: 13px; letter-spacing: 0.5px; }
  .social { position: absolute; right: 18px; top: 11px; display: flex; gap: 7px; }
  .social span { width: 32px; height: 32px; background: #e6e6e6; border-radius: 3px; border: 1px solid #bbb; }
</style>
</head>
<body>
  <header class="site-header">
    <div class="brand"><span class="brand-mark"></span><span class="brand-name">trelwirefix</span></div>
    <div class="search">
      <span>Search...</span>
      <svg width="24" height="24" viewBox="0 0 24 24" aria-hidden="true"><circle cx="9" cy="9" r="6.5" fill="none" stroke="#fff" stroke-width="2.5"/><line x1="14" y1="14" x2="21" y2="21" stroke="#fff" stroke-width="3.5" stroke-linecap="round"/></svg>
    </div>
  </header>

  <nav class="main-nav">
    <a>Home</a><a>About Us</a><a>Services</a><a>Our Work</a><a>Specials</a><a>Contact Us</a>
  </nav>

  <section class="hero">
    <div class="hero-photo" role="img" aria-label="Electricity transmission pylon against a blue sky with clouds"></div>
    <h1 class="hero-title">Reduce Your Electricity Bill<br>By<br>Lowering Your<br>Energy Consuption</h1>
    <svg class="hero-arrow prev" width="24" height="26" viewBox="0 0 24 26" aria-hidden="true"><polyline points="18,3 6,13 18,23" fill="none" stroke="#333" stroke-width="6"/></svg>
    <svg class="hero-arrow next" width="24" height="26" viewBox="0 0 24 26" aria-hidden="true"><polyline points="6,3 18,13 6,23" fill="none" stroke="#333" stroke-width="6"/></svg>
  </section>

  <article class="promo left">
    <h2>LED IS THE FUTURE</h2>
    <p>LED lighting has involved rapidly in the last 5 years. In the coming years we will see all lighting being substitued with LED lights. It is by far the most efficient form of lighting on todays market. Let us retrofit your business or home with LED and the savings will literally pay the lights off.</p>
  </article>
  <div class="btn dark" style="left:21px;top:640px;width:160px;">Why Led ?</div>
  <div class="btn green" style="left:202px;top:640px;width:160px;">Request Quote</div>

  <div class="divider-v"></div>

  <article class="promo right">
    <h2>REDUCE YOUR BUSINESS ENERGY CONSUMPTION</h2>
    <p>By letting us analyse your energy consumption, we can identify where you are simply burning your money. We can suggest and implement easy solutions to save you money and minimise your carbon emmissions.</p>
  </article>
  <div class="btn dark" style="left:554px;top:647px;width:203px;">Energy Efficient Audit</div>
  <div class="btn green" style="left:784px;top:647px;width:161px;">Book Audit Now</div>

  <div class="rule" style="top:721px;"></div>

  <section class="card" style="left:16px;">
    <h3>Electrical Contracting</h3>
    <p>We offer all types of electrical work<br>from Installation to maintenance.</p>
    <div class="card-icon"><span role="img" aria-label="Green power button icon" style="background:#7cc243;"></span></div>
    <a>View Our Services</a>
  </section>
  <section class="card" style="left:367px;">
    <h3>Energy Efficiency</h3>
    <p>With one of our audits to your business<br>or home we can lower your energy bills<br>and minimise your carbon footprint.</p>
    <div class="card-icon"><span role="img" aria-label="Green outline light bulb icon" style="background:#e4f4e6;"></span></div>
    <a>View Our Services</a>
  </section>
  <section class="card" style="left:718px;">
    <h3>Underground Locating</h3>
    <p>We have the tools and knowledge in<br>locating underground utilities.</p>
    <div class="card-icon"><span role="img" aria-label="Blue roadwork warning sign icon" style="background:#2f8fe0;"></span></div>
    <a>View Our Services</a>
  </section>

  <div class="rule" style="top:1032px;"></div>

  <nav class="footer-nav">Home<span>|</span>About Us<span>|</span>News<span>|</span>Blog<span>|</span>Specials<span>|</span>Testimonials<span>|</span>Contact Us</nav>

  <footer class="footer-bar">
    <div class="copyright">Copyright © 2013 trelwirefix.com</div>
    <div class="social" aria-label="Social links"><span></span><span></span><span></span><span></span><span></span></div>
  </footer>
</body>
</html>
```